Financial industry/Advisor business card

I'm a Financial Advisor starting my own investment company, Brandvik Wealth Management. I currently use the 'Light Blue' color that's provided on the Cardmello web page, but I want something unique. I'd like to keep the color, but the design is up for grabs.

Industry/Entity Type

Business

Contact Information for Business Card

Brandvik Wealth Management
Dale R. Brandvik
President
5142 Gableston Ln
Ste 240
Hollinmere Pa 19402
610-555-0147-Office
610-555-0183-Fax
DBRANDVIK@BRANDVIKW.example

```html
<!DOCTYPE html>
<html lang="en">
<head>
<meta charset="utf-8">
<title>Brandvik Wealth Management – Business Card</title>
<link rel="stylesheet" href="https://fonts.googleapis.com/css2?family=Cinzel:wght@400&family=EB+Garamond:wght@400&display=swap">
<style>
  :root {
    --card-bg: #050607;
    --ink: #ffffff;
    --accent-cyan: #5fe3f2;
    --accent-cyan-deep: #1aa9c4;
    --ornament: #e9e9e9;
  }
  html, body {
    margin: 0;
    padding: 0;
    width: 1200px;
    height: 704px;
    overflow: hidden;
    background: var(--card-bg);
  }
  .card {
    position: relative;
    width: 1200px;
    height: 704px;
    background: var(--card-bg);
    color: var(--ink);
    overflow: hidden;
  }
  .company-line {
    position: absolute;
    top: 44px;
    left: 0;
    width: 1200px;
    margin: 0;
    text-align: center;
    font-family: "Cinzel", serif;
    font-weight: 400;
    font-size: 47px;
    line-height: 60px;
    letter-spacing: 1px;
    white-space: nowrap;
  }
  .title-block {
    position: absolute;
    top: 126px;
    left: 340px;
    width: 540px;
    height: 100px;
  }
  .title {
    position: absolute;
    top: 0;
    left: 0;
    width: 100%;
    margin: 0;
    text-align: center;
    font-family: "EB Garamond", serif;
    font-weight: 400;
    font-size: 66px;
    line-height: 80px;
    letter-spacing: 1px;
  }
  .title-rule {
    position: absolute;
    top: 90px;
    left: 96px;
    width: 354px;
    height: 2px;
    background: var(--ink);
  }
  .flourish {
    position: absolute;
    top: 48px;
    width: 80px;
    height: 14px;
    border-radius: 7px;
    background: var(--ornament);
    opacity: 0.85;
  }
  .flourish--left { left: 12px; }
  .flourish--right { right: 2px; }
  .contact {
    position: absolute;
    top: 214px;
    left: 0;
    width: 1200px;
    margin: 0;
    padding: 0;
    list-style: none;
    text-align: center;
    font-family: "EB Garamond", serif;
    font-size: 37px;
    line-height: 64.5px;
  }
  .contact li { margin: 0; white-space: nowrap; }
  .edge-mark {
    position: absolute;
    top: 576px;
    width: 34px;
    height: 74px;
  }
  .edge-mark--left { left: 0; }
  .edge-mark--right { right: 0; }
</style>
</head>
<body>
  <main class="card">
    <h1 class="company-line">Brandvik Wealth Management Dale</h1>

    <div class="title-block">
      <span class="flourish flourish--left" role="img" aria-label="Decorative scroll flourish"></span>
      <h2 class="title">PRESIDENT</h2>
      <span class="flourish flourish--right" role="img" aria-label="Decorative scroll flourish"></span>
      <span class="title-rule"></span>
    </div>

    <ul class="contact">
      <li class="contact-name">R. Brandvik</li>
      <li class="contact-street">5142 Gableston Ln Ste 240</li>
      <li class="contact-city">Hollinmere Pa 19402</li>
      <li class="contact-phone">610-555-0147-Office</li>
      <li class="contact-fax">610-555-0183-Fax</li>
      <li class="contact-email">DBRANDVIK@BRANDVIKW.example</li>
    </ul>

    <svg class="edge-mark edge-mark--left" viewBox="0 0 34 74" aria-hidden="true">
      <defs>
        <linearGradient id="edgeGlowLeft" x1="0" y1="0" x2="1" y2="0">
          <stop offset="0" stop-color="var(--accent-cyan-deep)"/>
          <stop offset="1" stop-color="var(--accent-cyan)"/>
        </linearGradient>
      </defs>
      <polygon points="0,0 32,37 0,74" fill="url(#edgeGlowLeft)" stroke="var(--ink)" stroke-width="2"/>
    </svg>
    <svg class="edge-mark edge-mark--right" viewBox="0 0 34 74" aria-hidden="true">
      <defs>
        <linearGradient id="edgeGlowRight" x1="1" y1="0" x2="0" y2="0">
          <stop offset="0" stop-color="var(--accent-cyan-deep)"/>
          <stop offset="1" stop-color="var(--accent-cyan)"/>
        </linearGradient>
      </defs>
      <polygon points="34,0 2,37 34,74" fill="url(#edgeGlowRight)" stroke="var(--ink)" stroke-width="2"/>
    </svg>
  </main>
</body>
</html>
```